Dr. Pelham Billboard Sign Design

Family Dental Practice looking for a billboard sign design. We have Attached a Image of Dr Pelham and Her horse she would like to incorporate. The size of the sign is 118" tall and 196" Wide. We hired a previous designer to work on this also but would like to see what other come up with before we decide on a final. Please use something similar for a animal shelter icon to go beside the Animal Shelter Discount statement. You can use the text from the postcard file attached. I know text adjustments will be needed, but more interested in a eye catching design. Themes: Fall/Winter/Mountains/Nature , colors: open but Dr P like purple. We are open to ideas and will answer any questions.
TEXT
Theme: Fall/Winter/Mountain
Image: Dr Pelham with Horse (Same from mailer design)
Text to Keep that needs to be bold and Priority
1. Dr. Rosalind Pelham Family Dentistry
314 Brellin Court Spruce Pine, NC 28094
828-413-5276 | RPelhamDDS@Velmorx.net
(FaceBook icon) RosalindPelhamDDS
2. ACCEPTING NEW PATIENTS
3. Affordable Dentistry for Your Whole Family
4. WE FILE YOUR INSURANCE CLAIMS
5. Discounts for Senior Citizens, Law Enforcement, First Responders, Military Personnel, State Employees and College Students
6. (Cool Animal Shelter Icon) WE OFFER A DISCOUNT TO PATIENTS WHO SUPPORT OUR LOCAL ANIMAL SHELTERS BY ADOPTING, DONATING OR VOLUNTEERING
7. Schedule Your Appointment TODAY!
Target Market(s)
Local Community to Bring in Patients to dental office
Industry/Entity Type
Dental
Look and feel

```html
<!DOCTYPE html>
<html lang="en">
<head>
<meta charset="utf-8">
<title>Dr. Pelham Family Dentistry Billboard</title>
<link rel="stylesheet" href="https://fonts.googleapis.com/css2?family=Open+Sans:wdth,wght@75..100,400..800&display=swap">
<style>
  :root {
    --teal: #1f8796;
    --teal-dark: #176c79;
    --ink: #1d2a33;
    --blue: #1565c0;
    --badge: #1f3f8a;
    --grey-edge: #b9c4c9;
    --sky-top: #bfeaf6;
    --sky-deep: #3fb2cf;
    --panel-top: #ffffff;
    --panel-bottom: #dff1fa;
    --page: #f2f4f6;
  }
  * { margin: 0; padding: 0; box-sizing: border-box; }
  html, body { width: 850px; height: 1200px; overflow: hidden; background: var(--page); }
  body { position: relative; font-family: "Open Sans", Arial, sans-serif; color: var(--ink); }

  .billboard {
    position: absolute; left: 65px; top: 383px;
    width: 719px; height: 434px;
    overflow: hidden;
    box-shadow: 0 4px 14px rgba(0,0,0,.18);
    white-space: nowrap;
  }
  .billboard__art { position: absolute; inset: 0; }

  .header-band {
    position: absolute; left: 290px; top: 22px; width: 429px; height: 45px;
    background: var(--teal);
    color: #fff; font-weight: 700; font-stretch: 75%;
    font-size: 30px; line-height: 45px; text-align: center; letter-spacing: .2px;
  }
  .today {
    position: absolute; left: 326px; top: 70px;
    font-weight: 800; font-stretch: 75%; font-size: 62px; line-height: 66px;
    color: var(--teal-dark);
  }
  .practice { position: absolute; left: 529px; top: 76px; }
  .practice__name { font-weight: 700; font-stretch: 75%; font-size: 17px; color: var(--teal-dark); line-height: 20px; }
  .practice__kind { font-weight: 700; font-stretch: 75%; font-size: 15px; color: var(--ink); line-height: 19px; }
  .practice__social { display: flex; align-items: center; gap: 3px; font-weight: 700; font-stretch: 75%; font-size: 13px; line-height: 17px; color: var(--ink); }
  .practice__social .dot { width: 9px; height: 9px; border-radius: 50%; background: var(--blue); }

  .benefits { position: absolute; left: 346px; top: 146px; list-style: none; }
  .benefits li { display: flex; align-items: center; gap: 5px; font-size: 14px; line-height: 21px; color: var(--ink); }
  .benefits svg { width: 11px; height: 11px; flex: none; }

  .discounts { position: absolute; left: 358px; top: 214px; font-size: 11px; line-height: 16px; font-weight: 500; }
  .discounts b { font-weight: 700; }

  .shelter { position: absolute; left: 362px; top: 274px; width: 350px; height: 92px; }
  .shelter__badge {
    position: absolute; left: 0; top: 4px; width: 46px; height: 46px;
    background: var(--badge); border: 3px solid #fff; outline: 1px solid #8aa1b6;
  }
  .shelter__text { position: absolute; left: 54px; top: 0; }
  .shelter__lead { font-weight: 700; font-stretch: 75%; font-size: 25px; line-height: 26px; color: var(--teal); }
  .shelter__main { font-size: 19px; line-height: 24px; color: var(--ink); }
  .shelter__sub { font-size: 14.5px; line-height: 18px; color: var(--ink); }
  .shelter__bar {
    position: absolute; left: 54px; top: 71px; width: 276px; height: 16px;
    background: var(--blue); color: #fff; font-size: 9.4px; line-height: 16px; text-align: center; letter-spacing: .1px;
  }

  .contact { position: absolute; left: 348px; top: 368px; font-style: normal; }
  .contact__row { display: flex; align-items: center; gap: 6px; font-size: 15.5px; line-height: 25px; white-space: nowrap; }
  .contact__row svg { width: 13px; height: 13px; flex: none; }
  .contact__link { color: var(--blue); font-weight: 700; }
  .contact__sep { color: var(--ink); margin: 0 2px; }
</style>
</head>
<body>
  <main class="billboard">
    <svg class="billboard__art" viewBox="0 0 719 434" width="719" height="434">
      <defs>
        <linearGradient id="photoTone" x1="0" y1="0" x2="0.6" y2="1">
          <stop offset="0" stop-color="#bfeaf6"/>
          <stop offset="0.55" stop-color="#3fb2cf"/>
          <stop offset="1" stop-color="#e9f6fb"/>
        </linearGradient>
        <linearGradient id="panelTone" x1="0" y1="0" x2="0" y2="1">
          <stop offset="0" stop-color="#ffffff"/>
          <stop offset="1" stop-color="#dff1fa"/>
        </linearGradient>
      </defs>
      <rect class="photo-area" role="img" aria-label="Photo of Dr. Pelham standing with her brown horse in a snowy winter landscape with bare trees" x="0" y="0" width="360" height="434" fill="url(#photoTone)"/>
      <path class="curve-band" d="M282,0 C250,90 322,160 296,240 C276,305 282,380 284,434 L719,434 L719,0 Z" fill="#1f8796"/>
      <path class="curve-edge" d="M300,0 C268,90 340,160 314,240 C294,305 300,380 302,434" fill="none" stroke="#b9c4c9" stroke-width="4"/>
      <path class="panel" d="M304,0 C272,90 344,160 318,240 C298,305 304,380 306,434 L719,434 L719,0 Z" fill="url(#panelTone)"/>
    </svg>

    <div class="header-band">SCHEDULE YOUR APPOINTMENT</div>
    <div class="today">TODAY!</div>

    <div class="practice">
      <div class="practice__name">DR. ROSALIND PELHAM</div>
      <div class="practice__kind">FAMILY DENTISTRY</div>
      <div class="practice__social"><span class="dot"></span>RosalindPelhamDDS</div>
    </div>

    <ul class="benefits">
      <li><svg viewBox="0 0 12 12"><rect x="0.5" y="0.5" width="11" height="11" fill="none" stroke="#1f8796"/><path d="M2.5 6 L5 8.5 L10 2.5" fill="none" stroke="#1f8796" stroke-width="1.6"/></svg>ACCEPTING NEW PATIENTS</li>
      <li><svg viewBox="0 0 12 12"><rect x="0.5" y="0.5" width="11" height="11" fill="none" stroke="#1f8796"/><path d="M2.5 6 L5 8.5 L10 2.5" fill="none" stroke="#1f8796" stroke-width="1.6"/></svg>AFFORDABLE DENTISTRY FOR YOUR WHOLE FAMILY</li>
      <li><svg viewBox="0 0 12 12"><rect x="0.5" y="0.5" width="11" height="11" fill="none" stroke="#1f8796"/><path d="M2.5 6 L5 8.5 L10 2.5" fill="none" stroke="#1f8796" stroke-width="1.6"/></svg>WE FILE YOUR INSURANCE CLAIMS</li>
    </ul>

    <p class="discounts">Discounts for <b>Senior Citizens, Law Enforcement,</b><br><b>First Responders, Military Personnel, State Employees</b><br><b>and College Students</b></p>

    <section class="shelter">
      <div class="shelter__badge" role="img" aria-label="Animal shelter badge"></div>
      <div class="shelter__text">
        <div class="shelter__lead">WE OFFER</div>
        <div class="shelter__main">A DISCOUNT TO PATIENTS</div>
        <div class="shelter__sub">WHO SUPPORT OUR LOCAL ANIMAL</div>
      </div>
      <div class="shelter__bar">SHELTERS BY ADOPTING, DONATING OR VOLUNTEERING</div>
    </section>

    <address class="contact">
      <div class="contact__row">
        <svg viewBox="0 0 12 12"><path d="M6 11 C3 7.5 2 6 2 4.5 A4 4 0 0 1 10 4.5 C10 6 9 7.5 6 11 Z" fill="none" stroke="#555" stroke-width="1"/><circle cx="6" cy="4.5" r="1.4" fill="none" stroke="#555"/></svg>
        <span>314 Brellin Court Spruce Pine, NC 28094</span>
      </div>
      <div class="contact__row">
        <svg viewBox="0 0 12 12"><path d="M2.5 1.5 L4.5 1.5 L5.3 4 L4 5 C4.7 6.6 5.6 7.5 7 8 L8 6.7 L10.5 7.5 L10.5 9.5 C6 10 2 6 2.5 1.5 Z" fill="#333"/></svg>
        <span class="contact__link">828-413-5276</span>
        <span class="contact__sep">|</span>
        <svg viewBox="0 0 12 12"><rect x="1" y="2.5" width="10" height="7" fill="#333"/><path d="M1 2.5 L6 6.5 L11 2.5" fill="none" stroke="#fff" stroke-width="0.9"/></svg>
        <span class="contact__link">RPelhamDDS@Velmorx.net</span>
      </div>
    </address>
  </main>
</body>
</html>
```